Business Cards

Business card design for my company.
I would like the card's background colour to be black. You can also see our web site to get an idea of our brand. https://www.dlqmarrowfield.com.au/
- Name
- Email

```html
<!DOCTYPE html>
<html lang="en">
<head>
<meta charset="utf-8">
<title>DLQ Marrowfield Business Cards</title>
<link href="https://fonts.googleapis.com/css2?family=Poppins:wght@400;500;600;700&display=swap" rel="stylesheet">
<style>
  :root {
    --stage: #2a2a2d;
    --card: #222524;
    --green: #1f9a45;
    --white: #f4f4f4;
    --soft: #d9d9d9;
  }
  * { box-sizing: border-box; margin: 0; padding: 0; }
  html, body {
    width: 1200px; height: 800px; overflow: hidden;
    background: var(--stage);
    font-family: "Poppins", sans-serif;
  }
  .stage {
    width: 1200px; height: 800px;
    display: flex; align-items: center; justify-content: center; gap: 40px;
  }
  .card {
    position: relative;
    width: 540px; height: 310px;
    background: var(--card);
    border-radius: 18px;
    box-shadow: 0 18px 40px rgba(0,0,0,.45);
    color: var(--white);
    overflow: hidden;
  }
  /* brand lockup */
  .brand {
    display: flex; align-items: center; gap: 10px;
    font-weight: 600; color: var(--white);
    letter-spacing: .08em; text-transform: uppercase;
  }
  .brand-square { background: var(--green); flex: none; }

  /* front */
  .card-front {
    display: flex; flex-direction: column; align-items: center; justify-content: center;
  }
  .card-front .brand { font-size: 30px; }
  .card-front .brand-square { width: 22px; height: 22px; }
  .front-url {
    margin-top: 34px;
    font-size: 15px; font-weight: 400; letter-spacing: .18em;
    color: var(--soft);
  }

  /* back */
  .card-back .brand {
    position: absolute; top: 38px; right: 34px; font-size: 18px;
  }
  .card-back .brand-square { width: 14px; height: 14px; }
  .social {
    position: absolute; top: 92px; right: 34px; display: flex; gap: 6px;
  }
  .social span { width: 22px; height: 22px; background: var(--green); border-radius: 3px; }
  .person { position: absolute; top: 118px; left: 34px; }
  .person-name {
    font-size: 22px; font-weight: 600; color: var(--green);
    text-transform: uppercase; letter-spacing: .01em; line-height: 1.1;
  }
  .person-role {
    font-size: 13px; font-weight: 400; text-transform: uppercase;
    letter-spacing: .04em; margin-top: 2px;
  }
  .person-rule { width: 120px; height: 3px; background: var(--green); margin-top: 12px; }
  .contacts {
    position: absolute; left: 34px; bottom: 28px;
    list-style: none; display: flex; flex-direction: column; gap: 6px;
  }
  .contacts li { display: flex; align-items: center; gap: 10px; font-size: 13px; }
  .contact-icon {
    width: 18px; height: 18px; border-radius: 50%; background: var(--green);
    display: flex; align-items: center; justify-content: center; flex: none;
  }
  .contact-icon svg { width: 11px; height: 11px; }
</style>
</head>
<body>
<main class="stage">
  <section class="card card-front">
    <div class="brand"><span class="brand-square"></span>DLQ Marrowfield</div>
    <p class="front-url">www.dlqmarrowfield.com.au</p>
  </section>

  <section class="card card-back">
    <div class="brand"><span class="brand-square"></span>DLQ Marrowfield</div>
    <div class="social" aria-label="Social links"><span></span><span></span></div>

    <div class="person">
      <p class="person-name">Owen Tallis</p>
      <p class="person-role">General Manager</p>
      <div class="person-rule"></div>
    </div>

    <ul class="contacts">
      <li><span class="contact-icon"><svg viewBox="0 0 12 12"><rect x="3" y="1" width="6" height="10" rx="1.2" fill="none" stroke="#fff" stroke-width="1.3"/></svg></span>0400 123 456</li>
      <li><span class="contact-icon"><svg viewBox="0 0 12 12"><rect x="1" y="2.5" width="10" height="7" fill="none" stroke="#fff" stroke-width="1.2"/><path d="M1 2.5 6 7l5-4.5" fill="none" stroke="#fff" stroke-width="1.2"/></svg></span>info@dlqmarrowfield.com.au</li>
      <li><span class="contact-icon"><svg viewBox="0 0 12 12"><circle cx="6" cy="6" r="4.6" fill="none" stroke="#fff" stroke-width="1.2"/><path d="M1.4 6h9.2M6 1.4c2.4 2.6 2.4 6.6 0 9.2M6 1.4c-2.4 2.6-2.4 6.6 0 9.2" fill="none" stroke="#fff" stroke-width="1"/></svg></span>www.dlqmarrowfield.com.au</li>
      <li><span class="contact-icon"><svg viewBox="0 0 12 12"><path d="M6 11S2 7 2 4.6a4 4 0 0 1 8 0C10 7 6 11 6 11z" fill="#fff"/><circle cx="6" cy="4.6" r="1.4" fill="#1f9a45"/></svg></span>Eastvale, Tasmania, Australia</li>
    </ul>
  </section>
</main>
</body>
</html>
```